Website redesign for a Cloud Advisory business

We are looking to revisit our existing brand and website, with a view to updating both. Looking for concepts and designs for how the website might look, flow and feel. Current website is: www.brightlane.com.au

Scope and Deliverables: Concept design for the home page and one internal page.

We do not expect you to design all the pages and all the elements of the website at this stage.

This job is not for the full website design, but just for concepts that we can start with when we go into the full website design.

We would love to see a design feature based on our name, logo, or industry, which can run through banners and other collateral (chirpnet banner, ads on Findora, corporate documents etc).

We want the brand to properly depict what we bring/deliver to businesses when consulting to them and this should extend to the colour scheme, logo, font (perhaps updated) and copy (which will be supplied).

Our brand should suitably communicate our ability, knowledge and extensive experience within the Cloud space.

It should express and evoke credibility, knowledge and understanding of the Cloud space, independence, gravitas, reliability, efficiency, trust, expertise, approachability, service delivery but be uncomplicated, practical and use plain speaking language.

Colours that reinforce this might include: Blues, blacks, silver, white, grey and our existing orange.

Website designs that we like or have referenced include:

Skyvault: http://skyvault.com.au/ - This has good information but looks a little amateur in it’s cartoon like design and colour scheme. Also, this seems to be aimed at clients more interested in price than design and what we are going for is a little more high end.

Nimbuspath: https://www.nimbuspath.com.au/ - This site has merit in its’ setup but little call to action on the home page, especially before the scroll line. I like the set up of the Case Studies page however I’d look to make it more prominent by having it set up 3 across rather than the 4 they have. Something such as this: https://www.tallyrig.com/case-studies

Pelwyn: http://www.pelwyn.com.au/#home4 - This page is a good one as far as selling services and information on the company. I quite like it.

BorealIT: http://www.borealit.com.au/ - While I don’t think is particularly creative, it does practically depict the services we offer in a fairly clear way and might be a bit of a basic (albeit dull) template to follow.

QRV: https://store.qrv.com/us/Product-Family/QRV-Advisory-Services/QRV-Cloud-Advisory-Service/p/QRV-Services-Cloud-Advisory - This offers substantial information but is probably a little confusing although the roll-over drop down menus have merit.

LUP: http://www.lup.net.au/en/services/ - While this in not quite what we are looking for, the colour scheme gives it more gravitas and quality.

As another reference, this website and the way they present their case studies is also something we like, although I’d like them shown 3 up, side by side…. https://www.tallyrig.com/case-studies.

We have added a page layout and page purpose document.

Target Market(s)

Corporates, small - medium business, direct referrals, via search results

Industry/Entity Type

Business

Number of Pages Required

1 page

Font styles to use
Sans Serif

Colors
85abd2
0455a3
000000
f37122
5c5c5c

Requirements
Must have
• Website must be mobile device compatible.
• Concept design for the home page.
Nice to have
• We would love to see a design feature based on our name, logo, or industry, which can run through banners and other collateral (chirpnet banner, ads on Findora, corporate documents etc).

```html
<!DOCTYPE html>
<html lang="en">
<head>
<meta charset="utf-8">
<title>Brightlane – Impartial Cloud Solutions</title>
<link rel="stylesheet" href="https://fonts.googleapis.com/css2?family=Open+Sans:wght@400;600;700&family=Dancing+Script:wght@400&display=swap">
<style>
:root{
  --orange:#f15a24;
  --orange-soft:#f37122;
  --ink:#1b1b1b;
  --grey:#5c5c5c;
  --muted:#8a8a8a;
  --dark:#111315;
  --white:#ffffff;
}
*{box-sizing:border-box;margin:0;padding:0}
html,body{width:1200px;height:2740px;overflow:hidden}
body{position:relative;font-family:"Open Sans",Arial,sans-serif;background:var(--white);color:var(--grey)}
.abs{position:absolute}

/* navigation */
.site-nav{left:0;top:0;width:1200px;height:55px;background:var(--orange);display:flex;align-items:center;padding-left:91px;gap:37px}
.site-nav a{color:var(--white);font-size:14px;text-decoration:none}

/* hero */
.hero{left:0;top:55px;width:1200px;height:593px;background:linear-gradient(100deg,#b7b2ab 0%,#8d7a6c 30%,#c9c6c2 55%,#3a3a40 100%)}
.brand{left:91px;top:92px;display:flex;align-items:center;gap:12px}
.brand-mark{width:44px;height:44px;background:var(--orange)}
.brand-name{font-size:40px;font-weight:700;color:var(--ink);letter-spacing:1px}
.hero-caption{left:93px;top:334px;width:447px;height:133px;background:rgba(30,30,30,.82);padding:18px 16px}
.hero-caption h2{color:var(--white);font-size:28px;font-weight:700;line-height:1.1}
.hero-caption h2 span{color:var(--orange-soft)}
.hero-caption p{color:var(--white);font-size:13px;line-height:20px;margin-top:14px}

/* call to action band */
.cta-band{left:0;top:648px;width:1200px;height:225px;background:linear-gradient(90deg,#ee6a32,#f37a45 50%,#ee6a32);text-align:center}
.cta-band h1{color:var(--white);font-size:34px;font-weight:600;margin-top:32px;letter-spacing:.5px}
.cta-rule{width:370px;height:2px;background:rgba(255,255,255,.75);margin:10px auto 0}
.cta-band p{color:var(--white);font-size:13.5px;line-height:22px;width:830px;margin:16px auto 0}
.cta-button{left:489px;top:155px;width:209px;height:44px;background:var(--dark);display:flex;align-items:center;color:var(--white);font-size:13.5px}
.cta-button span{flex:1;text-align:center}
.cta-button i{width:34px;height:44px;border-left:1px solid #444;display:flex;align-items:center;justify-content:center}

/* services */
.service{width:190px;text-align:center;top:965px}
.service-icon{width:116px;height:116px;border:2px solid var(--orange);border-radius:50%;margin:0 auto;display:flex;align-items:center;justify-content:center}
.service h3{color:var(--orange);font-size:14px;font-weight:600;line-height:20px;height:42px;margin-top:20px}
.service p{font-size:12.5px;line-height:19px;color:var(--muted);margin-top:12px}
.service a{display:block;color:var(--orange);font-size:12.5px;margin-top:8px;text-decoration:none}

/* testimonial */
.testimonial{left:0;top:1320px;width:1200px;height:311px;background:linear-gradient(180deg,#1c1e21,#0b0c0e 60%,#17191b);text-align:center}
.testimonial h2{color:var(--white);font-size:21px;font-weight:600;margin-top:24px}
.rule-orange{width:120px;height:2px;background:var(--orange);margin:8px auto 0}
.quote-badge{width:66px;height:66px;border-radius:50%;background:var(--orange);margin:14px auto 0;display:flex;align-items:center;justify-content:center}
.testimonial p{color:#e6e6e6;font-size:12.5px;line-height:24px;width:900px;margin:18px auto 0}
.author{color:var(--orange-soft);font-size:13.5px;margin-top:14px}
.company{color:var(--white);font-size:13.5px;font-weight:600;margin-top:4px}

/* what we do */
.what-we-do{left:0;top:1631px;width:1200px;text-align:center}
.what-we-do h2{color:#333;font-size:18px;font-weight:600;margin-top:68px}
.what-we-do .rule-orange{width:96px}
.what-we-do p{font-size:12.5px;line-height:22px;color:#444;width:880px;margin:22px auto 0}
.product-visual{left:100px;top:1841px;width:430px;height:350px;background:linear-gradient(135deg,#1a1c22,#3b3426 55%,#c9cbcf 100%)}
.video-label{left:688px;top:1816px;font-family:"Dancing Script",cursive;font-size:36px;color:#333}
.video-frame{left:690px;top:1881px;width:413px;height:270px;background:linear-gradient(120deg,#c8c4bd,#e9e7e3 45%,#a08a70 100%)}
.play{left:872px;top:1992px}

/* contact */
.contact{left:0;top:2273px;width:1200px;height:420px;background:linear-gradient(180deg,#0c0d10,#1b1d22 60%,#0c0d10)}
.contact h2{position:absolute;left:0;width:1200px;text-align:center;top:26px;color:var(--white);font-size:17px;font-weight:600}
.contact .rule-orange{position:absolute;left:552px;top:60px;width:96px;margin:0}
.contact-item{left:94px;display:flex;align-items:center;gap:30px;color:var(--white);font-size:17px;line-height:24px}
.diamond{width:68px;height:68px;display:flex;align-items:center;justify-content:center}
.field{left:564px;width:541px;border:1px solid #555;background:rgba(0,0,0,.25);color:#7b7b7b;font-size:12px;padding:12px 14px}
.submit{left:564px;top:336px;width:110px;height:35px;background:var(--orange);color:var(--white);font-size:15px;font-weight:600;display:flex;align-items:center;justify-content:center}

.site-footer{left:0;top:2693px;width:1200px;height:47px;background:var(--orange);color:var(--white);font-size:11px;display:flex;align-items:center;justify-content:center}
</style>
</head>
<body>

<nav class="site-nav abs">
  <a href="#">Home</a><a href="#">About Us</a><a href="#">Industry Specialties</a><a href="#">Solutions</a><a href="#">The Company We Keep</a><a href="#">Case Studies and Testimonials</a><a href="#">FAQ's</a><a href="#">Blog</a><a href="#">Contact Us</a>
</nav>

<section class="hero abs" role="img" aria-label="Three business consultants talking in a bright city office"></section>
<div class="brand abs"><div class="brand-mark"></div><div class="brand-name">BRIGHTLANE</div></div>
<div class="hero-caption abs">
  <h2>IMPARTIAL CLOUD <span>SOLUTIONS</span></h2>
  <p>Sed ut perspiciatis unde omnis iste natus error sit voluptatem accu-<br>santium doloremque laudantium, totam rem aperiam,</p>
</div>

<section class="cta-band abs">
  <h1>IMPARTIAL CLOUD SOLUTIONS</h1>
  <div class="cta-rule"></div>
  <p>Sed ut perspiciatis unde omnis iste natus error sit voluptatem accusantium doloremque laudantium, totam rem aperiam, eaque ipsa quae ab illo inventore veritatis et quasi architecto beatae vitae dicta sunt explicabo.</p>
  <div class="cta-button abs"><span>Book A free Consultaion</span><i><svg width="14" height="10" viewBox="0 0 14 10"><path d="M0 5h12M8 1l4 4-4 4" stroke="#fff" stroke-width="1.6" fill="none"/></svg></i></div>
</section>

<div class="service abs" style="left:75px">
  <div class="service-icon"><svg width="40" height="54" viewBox="0 0 40 54"><path d="M20 2C20 2 3 26 3 36a17 17 0 0 0 34 0C37 26 20 2 20 2z" fill="#f15a24"/></svg></div>
  <h3>System Selection</h3>
  <p>Lorem ipsum dolor sit amet, consectetur adipiscing elit, sed do eiusmod tempor</p>
  <a href="#">Read More ›</a>
</div>
<div class="service abs" style="left:296px">
  <div class="service-icon"><svg width="40" height="52" viewBox="0 0 40 52"><rect x="2" y="2" width="36" height="48" rx="3" fill="none" stroke="#f15a24" stroke-width="3"/><rect x="8" y="8" width="24" height="9" fill="#f15a24"/><g fill="#f15a24"><rect x="8" y="22" width="6" height="5"/><rect x="17" y="22" width="6" height="5"/><rect x="26" y="22" width="6" height="5"/><rect x="8" y="31" width="6" height="5"/><rect x="17" y="31" width="6" height="5"/><rect x="26" y="31" width="6" height="5"/><rect x="8" y="40" width="6" height="5"/><rect x="17" y="40" width="6" height="5"/><rect x="26" y="40" width="6" height="5"/></g></svg></div>
  <h3>Accounting Systems<br>&amp; Conversions</h3>
  <p>Lorem ipsum dolor sit amet, consectetur adipiscing elit, sed do eiusmod tempor</p>
  <a href="#">Read More ›</a>
</div>
<div class="service abs" style="left:508px">
  <div class="service-icon"><svg width="54" height="48" viewBox="0 0 54 48"><rect x="2" y="2" width="50" height="34" rx="2" fill="#f15a24"/><rect x="7" y="7" width="40" height="24" fill="#fff"/><rect x="22" y="36" width="10" height="7" fill="#f15a24"/><rect x="14" y="43" width="26" height="4" fill="#f15a24"/></svg></div>
  <h3>Integration</h3>
  <p>Lorem ipsum dolor sit amet, consectetur adipiscing elit, sed do eiusmod tempor</p>
  <a href="#">Read More ›</a>
</div>
<div class="service abs" style="left:718px">
  <div class="service-icon"><svg width="60" height="60" viewBox="0 0 60 60"><g stroke="#f15a24" stroke-width="2.5" fill="none"><circle cx="30" cy="28" r="14"/><path d="M24 42v8h12v-8M25 54h10M30 4v6M10 12l4 4M50 12l-4 4M4 28h6M50 28h6"/></g><text x="30" y="34" text-anchor="middle" font-family="Open Sans,sans-serif" font-size="16" font-weight="700" fill="#f15a24">$</text></svg></div>
  <h3>Business Inventory</h3>
  <p>Lorem ipsum dolor sit amet, consectetur adipiscing elit, sed do eiusmod tempor</p>
  <a href="#">Read More ›</a>
</div>
<div class="service abs" style="left:933px">
  <div class="service-icon"><svg width="60" height="44" viewBox="0 0 60 44"><g fill="#f15a24"><circle cx="30" cy="10" r="8"/><path d="M16 40c0-12 6-18 14-18s14 6 14 18z"/><circle cx="12" cy="16" r="6"/><path d="M1 40c0-10 4-14 11-14 3 0 5 1 6 2-3 3-4 7-4 12z"/><circle cx="48" cy="16" r="6"/><path d="M59 40c0-10-4-14-11-14-3 0-5 1-6 2 3 3 4 7 4 12z"/></g></svg></div>
  <h3>Business Project &amp;<br>Job Management</h3>
  <p>Lorem ipsum dolor sit amet, consectetur adipiscing elit, sed do eiusmod tempor</p>
  <a href="#">Read More ›</a>
</div>

<section class="testimonial abs" role="img" aria-label="Dark boardroom with empty chairs behind a client quote">
  <h2>Testimonial</h2>
  <div class="rule-orange"></div>
  <div class="quote-badge"><svg width="38" height="32" viewBox="0 0 38 32"><g fill="none" stroke="#fff" stroke-width="2.4" stroke-linejoin="round"><path d="M3 3h22v14H12l-6 5v-5H3z"/><path d="M25 10h10v13h-3v5l-6-5H14v-3"/></g></svg></div>
  <p>Lorem ipsum dolor sit amet, consectetur adipiscing elit, sed do eiusmod tempor incididunt ut labore et dolore magna aliqua. Ut enim ad minim velit esse cillum dolore eu fugiat nulla pariatur. Excepteur sint occaecat cupidatat non proident, sunt in culpa qui officia deserunt mollit anim id est laborum Sed ut perspiciatis unde omnis iste natus error sit voluptatem doloremque.</p>
  <div class="author">By John Doe</div>
  <div class="company">Company Name</div>
</section>

<section class="what-we-do abs">
  <h2>WHAT WE DO</h2>
  <div class="rule-orange"></div>
  <p>Lorem ipsum dolor sit amet, consectetur adipiscing elit, sed do eiusmod tempor incididunt ut labore et dolore magna aliqua. Ut enim ad minim veniam, quis nostrud exercitation ullamco laboris nisi ut aliquip ex ea commodo consequat.</p>
</section>
<div class="product-visual abs" role="img" aria-label="Desktop monitor showing a business growth dashboard"></div>
<div class="video-label abs">Click For Play Video</div>
<div class="video-frame abs" role="img" aria-label="Video still of a man working at a laptop in a library office"></div>
<svg class="play abs" width="48" height="48" viewBox="0 0 48 48"><circle cx="24" cy="24" r="22" fill="rgba(255,255,255,.15)" stroke="#fff" stroke-width="2"/><path d="M18 13l15 11-15 11z" fill="#f15a24"/></svg>

<section class="contact abs" role="img" aria-label="Night city skyline behind the contact details">
  <h2>GET IN TUCH</h2>
  <div class="rule-orange"></div>

  <div class="contact-item abs" style="top:103px">
    <div class="diamond"><svg width="68" height="68" viewBox="0 0 68 68"><rect x="14" y="14" width="40" height="40" transform="rotate(45 34 34)" fill="#fff"/><path d="M26 24c2-2 4-2 5 0l2 4c1 2 0 3-1 4 1 3 3 5 6 6 1-1 2-2 4-1l4 2c2 1 2 3 0 5-3 3-8 2-13-3s-6-10-7-17z" fill="#f15a24"/></svg></div>
    <span>955.010.2731</span>
  </div>
  <div class="contact-item abs" style="top:195px">
    <div class="diamond"><svg width="68" height="68" viewBox="0 0 68 68"><rect x="14" y="14" width="40" height="40" transform="rotate(45 34 34)" fill="#fff"/><rect x="22" y="26" width="24" height="16" fill="#f15a24"/><path d="M22 26l12 9 12-9" stroke="#fff" stroke-width="1.6" fill="none"/></svg></div>
    <span>info@brightlane.com.au</span>
  </div>
  <div class="contact-item abs" style="top:286px">
    <div class="diamond"><svg width="68" height="68" viewBox="0 0 68 68"><rect x="14" y="14" width="40" height="40" transform="rotate(45 34 34)" fill="#fff"/><path d="M34 20a9 9 0 0 0-9 9c0 7 9 17 9 17s9-10 9-17a9 9 0 0 0-9-9z" fill="#f15a24"/><circle cx="34" cy="29" r="3.5" fill="#fff"/></svg></div>
    <span>Melbourne, Victoria<br>1300 000 418</span>
  </div>

  <div class="field abs" style="top:112px;height:44px">Full Name</div>
  <div class="field abs" style="top:176px;height:44px">Email Address</div>
  <div class="field abs" style="top:241px;height:74px">Message</div>
  <div class="submit abs">SUBMIT</div>
</section>

<footer class="site-footer abs">Copyright © 2014. All Rights Reserved</footer>

</body>
</html>
```